Pinecrest Bullion Website 3 Page Concept

We need a concept design for a company in Birmingham, AL called Pinecrest Bullion Works. We buy/sell precious metals, coins, fine watches, and jewelry. The current website can be found here: https://www.pinecrestbullionworks.example. We're looking to modernize the website, drawing inspiration from the websites KORVATH (https://www.korvath.example/) and TR Ingotry (https://www.tringotry.example/).

KORVATH has a lot of the design qualities we're looking to integrate into our website, with a similar header (from the changing metal prices to the categories).

+Pages to Be Designed for Concept
Home Page
Products Page
Main Store Page

+Colors
Black, White, Sleek Grey (from attached file), "Gold" (Citrus from attached file)

**Main goal is for the website to be easy to navigate and user friendly.

Target Market(s)

Retail customers

Industry/Entity Type

Coin

Number of Pages Required

3 page

Requirements
Must have
• +Colors
• Black, White, Sleek Grey (from attached file), "Gold" (Citrus from attached file)
• +The website would have 3 main sections (Coins, Fine Watches, and Jewelry). :
• -E-commerce (shopping cart link, etc.)
• -Account sign in option on front page
• -Variable payment pricing for gold/silver items (wire/cash, Paypal/CC, Coindash(Bitcoin)) (like so: https://www.korvath.example/product/58213/1-oz-silver-round-heron?27481=2)
• - Social media buttons (facebook, instagram)
• -Integrate same PBW logo from current website into new website design
• -Drop-down navigation menu towards the top for each 3 main sections (Hovering over them would list further categories), that lists further categories (can be taken from the left side of current site for example purposes: https://www.pinecrestbullionworks.example)
• Additional: Mobile Friendly!
• **Main goal is for the website to be easy to navigate and user friendly.
Nice to have
• Videos and links (blog - like) on the home page

```html
<!DOCTYPE html>
<html lang="en">
<head>
<meta charset="utf-8">
<title>Pinecrest Bullion Works — Home</title>
<link href="https://fonts.googleapis.com/css2?family=Montserrat:wght@300;400;500;600;700&family=Open+Sans:wght@400;600&display=swap" rel="stylesheet">
<style>
:root{
  --black:#111;
  --ink:#222;
  --grey:#6f6f6f;
  --sleek:#ececec;
  --line:#dcdcdc;
  --gold:#f5b820;
  --white:#fff;
  --silver-hi:#f6f6f6;
  --silver-lo:#cfcfcf;
}
*{box-sizing:border-box;margin:0;padding:0}
html,body{width:1200px;height:3789px;overflow:hidden;background:var(--white)}
body{font-family:"Open Sans",Arial,sans-serif;color:var(--ink);position:relative}
.wrap{position:absolute;left:40px;right:40px}
h1,h2,h3,.mont{font-family:"Montserrat",Arial,sans-serif}
.btn{display:inline-block;background:var(--gold);color:var(--white);font-family:"Montserrat",sans-serif;font-weight:600;text-transform:uppercase}

/* top bar */
.topbar{position:absolute;top:0;left:0;width:1200px;height:38px;border-bottom:1px solid var(--line);font-size:11px;color:var(--grey)}
.social{position:absolute;left:40px;top:13px;display:flex;gap:12px}
.social span{width:11px;height:11px;border-radius:50%;background:#9a9a9a}
.promo{position:absolute;right:40px;top:12px}

/* header */
.header{position:absolute;top:38px;left:0;width:1200px;height:139px;border-bottom:1px solid var(--line)}
.logo{position:absolute;left:40px;top:14px;display:flex;align-items:center;gap:12px}
.logo .mark{width:110px;height:110px;border-radius:50%;background:var(--black)}
.logo .name{font-family:"Montserrat",sans-serif;font-weight:700;font-size:22px;color:var(--black)}
.info{position:absolute;left:522px;top:0;width:360px;height:139px;border-left:1px solid var(--line);border-right:1px solid var(--line)}
.info .row{position:absolute;left:0;right:0;height:69px;display:flex;align-items:center;gap:18px;padding-left:20px;font-size:10px;color:var(--grey)}
.info .row+.row{top:69px;border-top:1px solid var(--line)}
.info b{color:var(--ink);font-size:10px;font-family:"Montserrat",sans-serif}
.acct{position:absolute;left:882px;top:0;right:40px;height:69px;display:flex;align-items:center;justify-content:space-around;font-size:10px}
.acct b{display:block;font-family:"Montserrat",sans-serif;font-size:11px}
.acct small{color:var(--grey)}
.search{position:absolute;left:896px;top:84px;right:40px;height:36px;border:1px solid var(--line);font-size:10px;color:#aaa;padding:11px 12px}

/* nav */
.nav{position:absolute;top:177px;left:0;width:1200px;height:50px;border-bottom:1px solid var(--line)}
.cats{position:absolute;left:40px;top:8px;width:230px;height:34px;border:1px solid var(--line);font:600 11px "Montserrat",sans-serif;padding:10px 14px;display:flex;justify-content:space-between;align-items:center}
.menu{position:absolute;left:286px;top:0;height:50px;display:flex;align-items:center;list-style:none;font:600 11px "Montserrat",sans-serif;text-transform:uppercase}
.menu li{padding:0 19px;border-left:1px solid var(--line);line-height:16px}
.menu li:first-child{border:0}

/* ticker */
.ticker{position:absolute;top:227px;left:0;width:1200px;height:69px;background:var(--black);color:var(--white);font:600 11px "Montserrat",sans-serif}
.ticker .metal{position:absolute;top:27px;display:flex;align-items:center;gap:10px}
.ticker .ingot{width:26px;height:14px;background:#cfcfcf;clip-path:polygon(18% 0,82% 0,100% 100%,0 100%)}
.ticker .metal i{font-style:normal;color:var(--gold)}
.btc{position:absolute;right:40px;top:22px;display:flex;align-items:center;gap:10px;font-size:15px;font-weight:500}
.btc span{width:26px;height:26px;border-radius:50%;background:var(--gold)}

/* hero */
.hero{position:absolute;top:296px;left:0;width:1200px;height:444px;background:linear-gradient(90deg,#3a3a3a 0%,#262626 45%,#151515 100%)}
.hero .art{position:absolute;left:46px;top:40px;width:480px;height:340px;border-radius:3px;background:linear-gradient(170deg,#5b4d2c 0%,#b8922f 30%,#d7b349 48%,#9c9c9c 70%,#8c7a62 86%,#6a5b48 100%)}
.hero h1{position:absolute;left:596px;top:80px;color:var(--white);font-weight:400;font-size:50px;line-height:62px}
.hero p{position:absolute;left:596px;top:218px;color:#eee;font-size:17px}
.hero .btn{position:absolute;left:596px;top:268px;padding:16px 40px;font-size:15px;font-weight:500}
.dots{position:absolute;left:574px;bottom:24px;display:flex;gap:8px}
.dots span{width:9px;height:9px;border-radius:50%;background:#777}
.dots span.on{background:var(--white)}

/* welcome */
.welcome{top:792px;text-align:center}
.welcome h2{font-weight:300;font-size:40px;letter-spacing:1px;color:#555}
.welcome h2 b{font-weight:400;color:var(--ink)}
.welcome p{margin:22px auto 0;font-family:"Montserrat",sans-serif;font-size:20px;line-height:37px;color:#666}

.tiles{top:1028px;height:136px;display:flex;gap:22px}
.tile{flex:1;background:var(--sleek);position:relative}
.tile .ph{position:absolute;left:18px;top:16px;width:132px;height:104px;background:linear-gradient(150deg,#f4f4f4,#d4d4d4 55%,#e6e6e6)}
.tile h3{position:absolute;left:158px;top:44px;font-size:18px;font-weight:700}
.tile .btn{position:absolute;left:158px;top:76px;font-size:9px;padding:6px 12px}

/* products */
.products{position:absolute;top:1230px;left:0;width:1200px;height:898px;background:linear-gradient(180deg,#2f2f2f,#1b1b1b)}
.tabs{position:absolute;top:28px;left:0;right:0;display:flex;justify-content:center;font:600 13px "Montserrat",sans-serif;color:var(--white);letter-spacing:1px}
.tabs span{padding:0 22px;border-left:1px solid #888}
.tabs span:first-child{border:0}
.arrow{position:absolute;top:26px;width:26px;height:26px;background:var(--white);display:flex;align-items:center;justify-content:center}
.grid{position:absolute;left:40px;right:40px;top:84px;display:grid;grid-template-columns:repeat(4,1fr);gap:20px 27px}
.card{background:var(--white);height:390px;position:relative;text-align:center}
.card .ph{position:absolute;left:22px;right:22px;top:22px;height:250px;background:linear-gradient(145deg,var(--silver-hi) 0%,var(--silver-lo) 55%,#ececec 100%)}
.card .title{position:absolute;left:0;right:0;top:306px;font-size:12px;color:#555}
.card .price{position:absolute;left:0;right:0;top:326px;font:500 21px "Montserrat",sans-serif}
.card.hover .ph{top:34px;height:196px;left:50px;right:50px}
.card.hover .title{top:262px}.card.hover .price{top:282px}
.card.hover .btn{position:absolute;left:50%;transform:translateX(-50%);top:324px;font-size:10px;padding:7px 14px}
.card .icons{position:absolute;right:12px;top:16px;display:flex;flex-direction:column;gap:12px}

/* badges */
.badges{top:2160px;height:70px;display:flex;justify-content:space-between;align-items:center;padding:0 30px}
.badges span{background:#e4e4e4}
.badges .wide{width:180px;height:44px;border-radius:3px}
.badges .round{width:70px;height:70px;border-radius:50%;background:#ededed}
.badges .tall{width:40px;height:66px;border-radius:3px;background:#d3dae4}

/* reviews */
.reviews{top:2278px;text-align:center}
.sect-title{font-weight:300;font-size:40px;color:#555;letter-spacing:1px}
.sect-title b{font-weight:400;color:var(--ink)}
.avatar{width:76px;height:76px;border-radius:50%;background:linear-gradient(160deg,#e3e3e3,#c8c8c8);margin:22px auto 0}
.quote{margin:26px auto 0;width:860px;font-size:13px;line-height:26px;color:#888}
.reviewer{margin-top:30px;font:700 14px "Montserrat",sans-serif;letter-spacing:1px}
.role{font-size:12px;color:#777;margin-top:8px}

/* video */
.video{top:2607px;height:381px;background:linear-gradient(180deg,#2a2a2a 0%,#4a4336 45%,#5e4d27 70%,#2c2c2c 100%)}
.video h2{position:absolute;top:108px;left:0;right:0;text-align:center;color:var(--white);font-weight:400;font-size:38px}
.video svg{position:absolute;left:510px;top:180px}

/* blog */
.blog{top:3006px}
.blog .sect-title{text-align:center}
.posts{display:flex;gap:28px;margin-top:24px}
.post{flex:1;height:220px;display:flex;background:#f4f4f4}
.post .ph{width:276px;height:220px;flex:none}
.post .txt{padding:20px 18px;font-size:11px;color:#777;line-height:19px}
.post h3{font-size:13px;color:var(--ink);letter-spacing:.5px}
.post .date{color:var(--gold);margin:6px 0 14px}
.post .more{margin-top:18px;font:600 10px "Montserrat",sans-serif;color:var(--ink)}

/* subscribe */
.subscribe{position:absolute;top:3372px;left:0;width:1200px;height:88px;border-bottom:1px solid var(--line);border-top:1px solid #f0f0f0}
.subscribe .label{position:absolute;left:310px;top:30px;display:flex;align-items:center;gap:14px;font:500 20px "Montserrat",sans-serif;letter-spacing:1px}
.subscribe .field{position:absolute;left:566px;top:24px;width:336px;height:40px;background:#f1f1f1}
.subscribe svg.send{position:absolute;left:866px;top:35px}

/* footer */
.footer{top:3490px;display:flex;justify-content:space-between;font-size:12px;color:#555}
.footer h4{font:700 13px "Montserrat",sans-serif;color:var(--ink);margin-bottom:24px}
.footer ul{list-style:none;line-height:23px}
.contact li{display:flex;gap:12px;align-items:flex-start;margin-bottom:10px;line-height:18px}
.contact svg{flex:none;margin-top:2px}
.bottom{position:absolute;top:3738px;left:0;width:1200px;height:51px;background:var(--black);color:var(--white);font-size:12px}
.bottom .copy{position:absolute;left:40px;top:18px}
.bottom .support{position:absolute;left:618px;top:16px;font:700 14px "Montserrat",sans-serif;display:flex;gap:14px;align-items:center}
.pay{position:absolute;right:40px;top:15px;display:flex;gap:5px}
.pay span{width:26px;height:18px;background:#ddd;border-radius:2px}
</style>
</head>
<body>

<div class="topbar">
  <div class="social"><span></span><span></span><span></span></div>
  <div class="promo">No More In-State Sales Tax on Gold/Silver Coins &amp; Bullion! Starting June 1st!</div>
</div>

<header class="header">
  <div class="logo"><span class="mark"></span><span class="name">PBW</span></div>
  <div class="info">
    <div class="row">
      <svg width="30" height="18" viewBox="0 0 30 18"><rect x="1" y="2" width="17" height="11" fill="none" stroke="#555" stroke-width="1.5"/><path d="M18 6h6l4 4v3h-10z" fill="none" stroke="#555" stroke-width="1.5"/><circle cx="7" cy="15" r="2" fill="#555"/><circle cx="23" cy="15" r="2" fill="#555"/></svg>
      <span>FREE SHIPPING<br>on orders $199+</span>
      <svg width="18" height="18" viewBox="0 0 18 18"><circle cx="9" cy="9" r="7.5" fill="none" stroke="#555" stroke-width="1.5"/><path d="M9 4v5h4" fill="none" stroke="#555" stroke-width="1.5"/></svg>
      <span>M-F 9-5<br>SAT 10-2</span>
    </div>
    <div class="row">
      <svg width="18" height="18" viewBox="0 0 18 18"><path d="M4 1l3 4-2 2c1 2 4 5 6 6l2-2 4 3-2 3C8 17 1 10 1 3z" fill="#333"/></svg>
      <b>CUSTOMER CARE :</b><span>205-555-0142 , 205-555-0187</span>
    </div>
  </div>
  <div class="acct">
    <div style="display:flex;gap:10px;align-items:center"><svg width="24" height="24" viewBox="0 0 24 24"><circle cx="12" cy="8" r="5" fill="none" stroke="#333" stroke-width="1.6"/><path d="M2 23c1-6 5-8 10-8s9 2 10 8" fill="none" stroke="#333" stroke-width="1.6"/></svg><div><b>ACCOUNT</b><small>Sign in / Register</small></div></div>
    <div style="display:flex;gap:10px;align-items:center"><svg width="24" height="24" viewBox="0 0 24 24"><path d="M1 3h4l3 13h12l3-9H7" fill="none" stroke="#333" stroke-width="1.6"/><circle cx="9" cy="20" r="2" fill="#333"/><circle cx="19" cy="20" r="2" fill="#333"/></svg><div><b>VIEW CART</b><small>0 items</small></div></div>
  </div>
  <div class="search">SEARCH PRODUCTS...</div>
</header>

<nav class="nav">
  <div class="cats"><span>ALL CATEGORIES</span><svg width="10" height="6" viewBox="0 0 10 6"><path d="M1 1l4 4 4-4" fill="none" stroke="#222" stroke-width="1.6"/></svg></div>
  <ul class="menu"><li>Home</li><li>About</li><li>Best Sellers</li><li>Precious Metals</li><li>Dealsrare</li><li>Coins</li><li>Sell to Us</li><li>FAQ</li><li>Contact</li></ul>
</nav>

<div class="ticker">
  <div class="metal" style="left:70px"><span class="ingot" style="background:var(--gold)"></span>GOLD <i>$1,329.41</i></div>
  <div class="metal" style="left:238px"><span class="ingot"></span>SILVER <i>$16.52</i></div>
  <div class="metal" style="left:372px"><span class="ingot"></span>PLATINUM <i>$958.24</i></div>
  <div class="metal" style="left:572px"><span class="ingot"></span>PALLADIUM <i>$988.96</i></div>
  <div class="btc"><span></span>Bitcoin Price $8801.17</div>
</div>

<section class="hero">
  <div class="art" role="img" aria-label="Gold bar with gold and silver coins on a wooden stand"></div>
  <h1>Lorem ipsum dolor<br>sita consecte</h1>
  <p>Lorem ipsum dolor sit amet consectetur adipiscing elit</p>
  <span class="btn">View More</span>
  <div class="dots"><span></span><span></span><span class="on"></span></div>
</section>

<section class="wrap welcome">
  <h2>WELCOME TO <b>PINECREST</b></h2>
  <p>We are a local family owned business that opened in 2011. We specialize in Coins, Estate Jewelry, Fine<br>Watches, Diamonds &amp; Precious Metals. Our goal is to treat every<br>customer as if they were our family.</p>
</section>

<section class="wrap tiles">
  <div class="tile"><div class="ph" role="img" aria-label="Gold and steel wristwatch"></div><h3>FINE WATCHES</h3><span class="btn">Order Now</span></div>
  <div class="tile"><div class="ph" role="img" aria-label="Diamond jewelry"></div><h3>FINE JEWELRY</h3><span class="btn">Order Now</span></div>
  <div class="tile"><div class="ph" role="img" aria-label="Sterling silver tableware"></div><h3>STERLING SILVER</h3><span class="btn">Order Now</span></div>
</section>

<section class="products">
  <span class="arrow" style="left:40px"><svg width="8" height="12" viewBox="0 0 8 12"><path d="M6 1L1 6l5 5" fill="none" stroke="#111" stroke-width="2"/></svg></span>
  <span class="arrow" style="right:40px"><svg width="8" height="12" viewBox="0 0 8 12"><path d="M2 1l5 5-5 5" fill="none" stroke="#111" stroke-width="2"/></svg></span>
  <div class="tabs"><span>FEATURED</span><span>LATEST</span><span>SPECIAL</span><span>BEST SELLER</span></div>
  <div class="grid">
    <div class="card"><div class="ph" role="img" aria-label="Silver round coin"></div><div class="title">1oz Generic .999 Silver Rounds</div><div class="price">$ 17.53</div></div>
    <div class="card"><div class="ph" role="img" aria-label="Silver eagle coin"></div><div class="title">1oz Generic .999 Silver Rounds</div><div class="price">$ 17.53</div></div>
    <div class="card"><div class="ph" role="img" aria-label="Commemorative silver coin"></div><div class="title">1oz Generic .999 Silver Rounds</div><div class="price">$ 17.53</div></div>
    <div class="card hover">
      <div class="icons">
        <svg width="14" height="13" viewBox="0 0 14 13"><path d="M7 12L1.5 6.5A3 3 0 017 2.5a3 3 0 015.5 4z" fill="none" stroke="#999" stroke-width="1.3"/></svg>
        <svg width="14" height="14" viewBox="0 0 14 14"><rect x="1" y="4" width="9" height="9" fill="none" stroke="#999" stroke-width="1.3"/><path d="M4 4V1h9v9h-3" fill="none" stroke="#999" stroke-width="1.3"/></svg>
        <svg width="14" height="10" viewBox="0 0 14 10"><path d="M1 5c3-5 9-5 12 0-3 5-9 5-12 0z" fill="none" stroke="#999" stroke-width="1.3"/><circle cx="7" cy="5" r="1.8" fill="#999"/></svg>
      </div>
      <div class="ph" role="img" aria-label="Maple leaf silver coin"></div><div class="title">1oz Generic .999 Silver Rounds</div><div class="price">$ 17.53</div><span class="btn">Add to Cart</span></div>
    <div class="card"><div class="ph" role="img" aria-label="Silver round coin"></div><div class="title">1oz Generic .999 Silver Rounds</div><div class="price">$ 17.53</div></div>
    <div class="card"><div class="ph" role="img" aria-label="Silver eagle coin"></div><div class="title">1oz Generic .999 Silver Rounds</div><div class="price">$ 17.53</div></div>
    <div class="card"><div class="ph" role="img" aria-label="Commemorative silver coin"></div><div class="title">1oz Generic .999 Silver Rounds</div><div class="price">$ 17.53</div></div>
    <div class="card hover">
      <div class="icons">
        <svg width="14" height="13" viewBox="0 0 14 13"><path d="M7 12L1.5 6.5A3 3 0 017 2.5a3 3 0 015.5 4z" fill="none" stroke="#999" stroke-width="1.3"/></svg>
        <svg width="14" height="14" viewBox="0 0 14 14"><rect x="1" y="4" width="9" height="9" fill="none" stroke="#999" stroke-width="1.3"/><path d="M4 4V1h9v9h-3" fill="none" stroke="#999" stroke-width="1.3"/></svg>
        <svg width="14" height="10" viewBox="0 0 14 10"><path d="M1 5c3-5 9-5 12 0-3 5-9 5-12 0z" fill="none" stroke="#999" stroke-width="1.3"/><circle cx="7" cy="5" r="1.8" fill="#999"/></svg>
      </div>
      <div class="ph" role="img" aria-label="Maple leaf silver coin"></div><div class="title">1oz Generic .999 Silver Rounds</div><div class="price">$ 17.53</div><span class="btn">Add to Cart</span></div>
  </div>
</section>

<section class="wrap badges" aria-label="Memberships and accreditations">
  <span class="wide"></span><span class="round"></span><span class="tall"></span><span class="wide"></span><span class="round"></span><span class="tall"></span>
</section>

<section class="wrap reviews">
  <h2 class="sect-title">CLIENT <b>REVIEWS</b></h2>
  <div class="avatar" role="img" aria-label="Reviewer portrait"></div>
  <p class="quote">&ldquo; There are many variations of passages of Lorem Ipsum available, but the majority have suffered alteration in some form, by injected or passages ofeven alteration in some form, by injected of passages ofeven slightly available.Duis aute irure dolor in.. &rdquo;</p>
  <div class="reviewer">DARIN HOLT</div>
  <div class="role">Mobile Developer</div>
</section>

<section class="wrap video" role="img" aria-label="Hand holding a gold coin, video still">
  <h2>Lorem ipsum dolor sit amet</h2>
  <svg width="100" height="100" viewBox="0 0 100 100"><circle cx="50" cy="50" r="46" fill="none" stroke="#fff" stroke-width="2.5"/><path d="M40 32l28 18-28 18z" fill="none" stroke="#fff" stroke-width="2.5"/></svg>
</section>

<section class="wrap blog">
  <h2 class="sect-title">LATEST <b>BLOG</b></h2>
  <div class="posts">
    <article class="post"><div class="ph" role="img" aria-label="Bitcoin coin on a dark surface" style="background:linear-gradient(160deg,#5a554f 0%,#9c7c45 50%,#3f3b37 100%)"></div><div class="txt"><h3>LOREM IPSUM DOLOR SIT</h3><div class="date">18 Jan, 2017</div>Lorem ipsum dolor sit amet, consectetur adipiscing elit. Aliquam facilisis ornare mi<div class="more">READ MORE</div></div></article>
    <article class="post"><div class="ph" role="img" aria-label="Stacks of gold coins" style="background:linear-gradient(135deg,#e6c06a,#b98a35 55%,#8a5f1f)"></div><div class="txt"><h3>LOREM IPSUM DOLOR SIT</h3><div class="date">04 Feb, 2017</div>Lorem ipsum dolor sit amet, consectetur adipiscing elit. Aliquam facilisis ornare mi<div class="more">READ MORE</div></div></article>
  </div>
</section>

<section class="subscribe">
  <div class="label"><svg width="34" height="24" viewBox="0 0 34 24"><rect x="1.5" y="1.5" width="31" height="21" fill="none" stroke="#222" stroke-width="2"/><path d="M2 2l15 11L32 2" fill="none" stroke="#222" stroke-width="2"/></svg>SUBSCRIBE US</div>
  <div class="field"></div>
  <svg class="send" width="22" height="20" viewBox="0 0 22 20"><path d="M1 9L21 1l-5 18-5-7z M11 12l10-11" fill="none" stroke="#222" stroke-width="1.6"/></svg>
</section>

<footer class="wrap footer">
  <div><h4>CONTACT US</h4>
    <ul class="contact">
      <li><svg width="14" height="18" viewBox="0 0 14 18"><path d="M7 17C2 11 1 8 1 6a6 6 0 0112 0c0 2-1 5-6 11z" fill="#666"/><circle cx="7" cy="6" r="2" fill="#fff"/></svg><span>418 Larkspur Ave<br>Fairhaven, AL 35990</span></li>
      <li><svg width="14" height="14" viewBox="0 0 18 18"><path d="M4 1l3 4-2 2c1 2 4 5 6 6l2-2 4 3-2 3C8 17 1 10 1 3z" fill="#666"/></svg><span>205-555-0142<br>205-555-0187</span></li>
      <li><svg width="14" height="12" viewBox="0 0 14 12"><rect width="14" height="12" fill="#666"/><path d="M0 0l7 6 7-6" fill="none" stroke="#fff"/></svg><span>pinecrestbullion@mail.example</span></li>
    </ul>
    <div class="social" style="position:static;margin-top:4px"><span></span><span></span><span></span></div>
  </div>
  <div><h4>MY ACCOUNT</h4><ul><li>Account</li><li>Login</li><li>Track an Order</li><li>Order</li><li>History</li><li>Price Alerts</li><li>Storage</li></ul></div>
  <div><h4>ABOUT US</h4><ul><li>About PBW</li><li>Careers</li><li>Blog</li><li>Our Pricing</li><li>Shipping &amp; Insurance</li><li>Payment</li><li>Methods</li></ul></div>
  <div><h4>BUYING &amp; SELLING</h4><ul><li>Precious Metals IRA</li><li>Coin Values</li><li>Sell to Us</li><li>Storage</li><li>International</li><li>Club</li><li>Reviews</li></ul></div>
  <div><h4>CUSTOMER CARE</h4><ul><li>Home</li><li>Contact Us</li><li>My Account</li><li>Privacy Policy</li><li>Terms &amp; Conditions</li></ul></div>
</footer>

<div class="bottom">
  <div class="copy">Copyright &copy; 2018 . All Rights Reserved.</div>
  <div class="support"><svg width="18" height="14" viewBox="0 0 18 14"><rect width="18" height="14" fill="#fff"/><path d="M0 0l9 7 9-7" fill="none" stroke="#111" stroke-width="1.5"/></svg>24hr Customer Support</div>
  <div class="pay" aria-label="Accepted payment methods"><span></span><span></span><span></span><span></span><span></span></div>
</div>

</body>
</html>
```